Flyer for an anniversary promotion

2nd year anniversary promotion flyer for Quarrywind Dental (logo attached)
Size A4
Promotion runs from Now until 31st Dec 2024
Leave room for actual promotional text which will be in multiple languages (~50 words)
Brand associations
Modern, classy, high quality service, customer care

NOTE - Company SELLS to dental clinics but Quarrywind is a dental products company, not dentists/dental clinics/etc.

Plentimarch wants this to be 300+ words

Target Market(s)

Dental clinics

Industry/Entity Type

Dental

Requirements
Should not have
• Don't use images of teeth

```html
<!DOCTYPE html>
<html lang="en">
<head>
<meta charset="utf-8">
<title>Quarrywind Dental – 2nd Year Anniversary Flyer</title>
<link rel="stylesheet" href="https://fonts.googleapis.com/css2?family=Cormorant+Garamond:wght@700&family=Great+Vibes&family=Catamaran:wght@700;800&family=Poppins:wght@700&family=Lato:wght@400&family=Noto+Serif+TC:wght@600&display=swap">
<style>
  :root {
    --page-bg: #e9ecef;
    --navy: #2a3590;
    --deep-blue: #1e5e91;
    --sky: #a9d6ef;
    --sky-light: #cfeaf8;
    --pale: #d3ecf8;
    --corner-blue: #2a78c6;
    --accent-blue: #3a8cc9;
    --stripe-green: #1fb38a;
    --stripe-blue: #1e77c4;
    --stripe-teal: #15b3c0;
    --body-text: #2b3a67;
    --white: #ffffff;
  }
  * { margin: 0; padding: 0; box-sizing: border-box; }
  html, body { width: 1200px; height: 856px; overflow: hidden; }
  body { background: var(--page-bg); position: relative; }

  .flyer {
    position: absolute;
    left: 310px;
    top: 18px;
    width: 868px;
    height: 1227px;
    transform: scale(0.668);
    transform-origin: top left;
    overflow: hidden;
    background: radial-gradient(ellipse at 45% 55%, var(--sky-light) 0%, var(--sky) 75%, #95c8e8 100%);
    box-shadow: 0 6px 18px rgba(0,0,0,.18);
  }
  .flyer__backdrop { position: absolute; inset: 0; width: 868px; height: 1227px; }

  .brand { position: absolute; left: 0; right: 0; text-align: center; font-family: "Cormorant Garamond", serif; font-weight: 700; color: var(--navy); }
  .brand__mark { display: block; margin: 0 auto; border-radius: 50%; background: var(--navy); }
  .brand__name { display: block; letter-spacing: 2px; line-height: 1; }
  .brand__sub { display: block; letter-spacing: 6px; line-height: 1; }

  .brand--top { top: 34px; }
  .brand--top .brand__mark { width: 120px; height: 120px; margin-bottom: 36px; }
  .brand--top .brand__name { font-size: 50px; }
  .brand--top .brand__sub { font-size: 30px; margin-top: 6px; }

  .brand--footer { top: 1060px; }
  .brand--footer .brand__mark { width: 70px; height: 70px; margin-bottom: 16px; }
  .brand--footer .brand__name { font-size: 32px; }
  .brand--footer .brand__sub { font-size: 20px; margin-top: 2px; }

  .script { position: absolute; font-family: "Great Vibes", cursive; color: var(--navy); line-height: 1; white-space: nowrap; }
  .script--lets { left: 215px; top: 300px; font-size: 130px; }
  .script--celebrate { left: 150px; top: 425px; font-size: 120px; }
  .script--our { left: 250px; top: 520px; font-size: 110px; }
  .script--anniversary { left: 228px; top: 590px; font-size: 130px; }

  .year-number { position: absolute; left: 405px; top: 250px; font-family: "Poppins", sans-serif; font-weight: 700; font-size: 420px; line-height: 1; color: var(--navy); }
  .year-tag { position: absolute; left: 418px; top: 563px; width: 232px; height: 34px; background: var(--navy); color: var(--white); font-family: "Catamaran", sans-serif; font-weight: 800; font-size: 28px; line-height: 34px; text-align: right; padding-right: 12px; }

  .tagline { position: absolute; left: 150px; top: 694px; font-family: "Catamaran", sans-serif; font-weight: 700; font-size: 32px; color: var(--accent-blue); white-space: nowrap; }
  .dates { position: absolute; left: 0; right: 0; top: 736px; text-align: center; padding-left: 22px; font-family: "Catamaran", sans-serif; font-weight: 800; font-size: 36px; color: var(--navy); }

  .promo { position: absolute; top: 800px; width: 350px; font-family: "Lato", sans-serif; font-size: 16.6px; line-height: 21px; color: var(--body-text); text-align: justify; }
  .promo--left { left: 62px; }
  .promo--right { left: 467px; }
  .promo__quote { font-family: Georgia, serif; font-weight: 700; font-size: 64px; line-height: 0; color: var(--navy); vertical-align: -18px; }
  .promo__quote--open { margin-right: 4px; }
  .promo__quote--close { margin-left: 4px; vertical-align: -30px; }

  .address { position: absolute; top: 1170px; font-weight: 700; color: var(--white); font-size: 14px; line-height: 20px; text-align: center; }
  .address--en { left: 25px; width: 295px; font-family: "Cormorant Garamond", serif; font-size: 15px; }
  .address--zh { left: 600px; width: 200px; text-align: left; font-family: "Noto Serif TC", serif; font-size: 15px; }
</style>
</head>
<body>
  <article class="flyer" aria-label="Quarrywind Dental second year anniversary flyer">
    <svg class="flyer__backdrop" viewBox="0 0 868 1227" aria-hidden="true">
      <defs>
        <linearGradient id="corner-left" x1="0" y1="1" x2="1" y2="0">
          <stop offset="0" stop-color="#1d62b8"/>
          <stop offset="1" stop-color="#5fb0ea"/>
        </linearGradient>
        <linearGradient id="corner-right" x1="0" y1="0" x2="1" y2="1">
          <stop offset="0" stop-color="#1d62b8"/>
          <stop offset="1" stop-color="#6bbcef"/>
        </linearGradient>
      </defs>
      <polygon points="0,0 868,0 868,255 429,8 0,255" fill="var(--pale)"/>
      <polygon points="0,0 250,0 0,155" fill="url(#corner-left)"/>
      <polygon points="868,0 612,0 868,155" fill="url(#corner-right)"/>
      <polygon points="429,8 868,255 868,160 612,0 250,0 0,160 0,255" fill="var(--pale)" opacity="0"/>
      <rect x="0" y="1037" width="289" height="13" fill="var(--stripe-green)"/>
      <rect x="289" y="1037" width="298" height="13" fill="var(--stripe-blue)"/>
      <rect x="587" y="1037" width="281" height="13" fill="var(--stripe-teal)"/>
      <rect x="0" y="1050" width="868" height="177" fill="var(--pale)"/>
      <polygon points="0,1155 328,1155 288,1227 0,1227" fill="var(--deep-blue)"/>
      <polygon points="558,1155 868,1155 868,1227 512,1227" fill="var(--deep-blue)"/>
    </svg>

    <header class="brand brand--top">
      <span class="brand__mark" aria-hidden="true"></span>
      <span class="brand__name">QUARRYWIND</span>
      <span class="brand__sub">DENTAL</span>
    </header>

    <h1 class="headline" aria-label="Let's celebrate our 2nd year anniversary">
      <span class="year-number" aria-hidden="true">2</span>
      <span class="year-tag" aria-hidden="true">nd Year</span>
      <span class="script script--lets" aria-hidden="true">Let’s</span>
      <span class="script script--celebrate" aria-hidden="true">celebrate</span>
      <span class="script script--our" aria-hidden="true">our</span>
      <span class="script script--anniversary" aria-hidden="true">anniversary</span>
    </h1>

    <p class="tagline">Come and Spend a day with us</p>
    <p class="dates">Now until 31st Dec 2024</p>

    <p class="promo promo--left"><span class="promo__quote promo__quote--open">“</span>Lorem ipsum dolor sit amet, consectetur adipiscing elit. Curabitur feugiat quis quam eget sodales. Cras iaculis posuere arcu quis venenatis. Maecenas tellus urna, pretium ac lacus sed, auctor fermentum est. Sed non dui velit. Integer quis blandit orci. Curabitur ornare risus tellus, vitae vestibulum leo imperdiet sit amet. Aenean tempor.<span class="promo__quote promo__quote--close">”</span></p>
    <p class="promo promo--right"><span class="promo__quote promo__quote--open">“</span>Lorem ipsum dolor sit amet, consectetur adipiscing elit. Curabitur feugiat quis quam eget sodales. Cras iaculis posuere arcu quis venenatis. Maecenas tellus urna, pretium ac lacus sed, auctor fermentum est. Sed non dui velit. Integer quis blandit orci. Curabitur ornare risus tellus, vitae vestibulum leo imperdiet sit amet. Aenean tempor.<span class="promo__quote promo__quote--close">”</span></p>

    <footer class="footer">
      <div class="brand brand--footer">
        <span class="brand__mark" aria-hidden="true"></span>
        <span class="brand__name">QUARRYWIND</span>
        <span class="brand__sub">DENTAL</span>
      </div>
      <p class="address address--en">Unit 408, Harbourlight Centre, 215 Lantern Road<br>Sham Shui Po, Kowloon</p>
      <p class="address address--zh" lang="zh-Hant">九龍深水埗燈籠道215<br>號港光中心408室</p>
    </footer>
  </article>
</body>
</html>
```